Letterhead

Can you please design me a letterhead that I can use electronically in word as a template. I have attached my business card as I would like the design to reflect this logo.

```html
<!DOCTYPE html>
<html lang="en">
<head>
<meta charset="utf-8">
<title>corvana — Letterhead &amp; Business Card</title>
<link rel="stylesheet" href="https://fonts.googleapis.com/css2?family=Arimo:wght@400;700&family=PT+Sans:wght@400;700&family=Open+Sans:wght@400&display=swap">
<style>
  :root {
    --board: #6b6c70;
    --paper: #ffffff;
    --paper-body: #ececec;
    --brand-red: #b51f29;
    --brand-dark-red: #5c1419;
    --ink: #000000;
    --text-grey: #555555;
    --zoom-ring: #c9c9cb;
    --zoom-bg: #939497;
  }
  * { box-sizing: border-box; margin: 0; padding: 0; }
  html, body { width: 1200px; height: 900px; overflow: hidden; }
  body { background: var(--board); position: relative; font-family: "PT Sans", Arial, sans-serif; }

  /* Letterhead sheet */
  .sheet {
    position: absolute; width: 639px; height: 852px;
    background: var(--paper-body);
    box-shadow: 3px 4px 8px rgba(0,0,0,.35);
    transform-origin: 0 0;
  }
  .sheet--main { left: 27px; top: 26px; }
  .sheet__header { position: absolute; left: 0; top: 0; width: 100%; height: 101px; background: var(--paper); }
  .wordmark {
    position: absolute; font-family: "Open Sans", Arial, sans-serif; font-weight: 400;
    color: var(--brand-red); letter-spacing: -1px; line-height: 1; white-space: nowrap;
  }
  .sheet .wordmark { left: 25px; top: 12px; font-size: 70px; }
  .company-line {
    position: absolute; font-family: "Arimo", Arial, sans-serif; color: var(--ink);
    white-space: nowrap;
  }
  .sheet .company-line { left: 299px; top: 18px; font-size: 13px; }
  .contact-band { position: absolute; left: 297px; top: 36px; width: 342px; height: 50px; background: var(--brand-red); }
  .contact-band__block { position: absolute; left: 0; top: 0; width: 50px; height: 100%; background: var(--ink); }
  .contact-band__list { position: absolute; left: 63px; top: 5px; list-style: none; color: #fff; font-size: 12px; line-height: 13px; }
  .footer-bar { position: absolute; left: 10px; top: 831px; width: 619px; height: 10px; background: var(--brand-red); }
  .footer-bar::after { content: ""; position: absolute; right: 0; top: 0; width: 86px; height: 100%; background: var(--ink); }

  /* Business card */
  .card { position: absolute; left: 511px; width: 316px; height: 195px; box-shadow: 3px 4px 8px rgba(0,0,0,.4); overflow: hidden; }
  .card--front { top: 248px; background: var(--paper); }
  .card--back { top: 457px; background: radial-gradient(ellipse at 50% 45%, #2a2a2a 0%, #121212 60%, #050505 100%); }
  .card .wordmark { left: 0; width: 100%; text-align: center; font-size: 47px; }
  .card--front .wordmark { top: 42px; left: 79px; width: auto; text-align: left; }
  .card--back .wordmark { top: 68px; color: var(--brand-dark-red); }
  .card .company-line { left: 81px; top: 92px; font-size: 9px; }
  .card__name { position: absolute; left: 32px; top: 141px; font-size: 9.5px; font-weight: 700; color: var(--text-grey); white-space: nowrap; }
  .card__role { font-weight: 400; color: var(--brand-red); }
  .card__sep { font-weight: 400; color: var(--brand-red); padding: 0 2px; }
  .card__contact { position: absolute; left: 32px; top: 155px; font-size: 8px; color: var(--text-grey); white-space: nowrap; }
  .card__contact b { font-weight: 400; color: var(--brand-red); }
  .card__bar { position: absolute; left: 0; bottom: 0; width: 100%; height: 19px; background: var(--brand-red); }
  .card__bar::after { content: ""; position: absolute; right: 0; top: 0; width: 43px; height: 100%; background: var(--ink); }

  /* Detail views */
  .detail-label { position: absolute; left: 973px; top: 20px; font-size: 17px; color: #fff; transform: rotate(4deg); }
  .detail {
    position: absolute; left: 895px; width: 286px; height: 286px; border-radius: 50%;
    overflow: hidden; background: var(--zoom-bg);
    border: 5px solid var(--zoom-ring);
    box-shadow: 0 0 0 1px rgba(0,0,0,.15), 2px 3px 8px rgba(0,0,0,.35);
  }
  .detail--top { top: 40px; }
  .detail--top .sheet { left: 7px; top: 32px; transform: scale(.67); }
  .detail--side { top: 335px; }
  .detail--side .sheet { left: -338px; top: 52px; transform: scale(.9); }
</style>
</head>
<body>

  <section class="sheet sheet--main" aria-label="Letterhead">
    <header class="sheet__header">
      <div class="wordmark">corvana</div>
      <div class="company-line">Business Consultants Pty Ltd</div>
      <div class="contact-band">
        <span class="contact-band__block"></span>
        <ul class="contact-band__list">
          <li>P : 0400 512 384</li>
          <li>E : maren@corvana.net.au</li>
          <li>ACN : 012 345 678</li>
        </ul>
      </div>
    </header>
    <div class="footer-bar"></div>
  </section>

  <section class="card card--front" aria-label="Business card front">
    <div class="wordmark">corvana</div>
    <div class="company-line">Business Consultants Pty Ltd</div>
    <div class="card__name">Maren Ellwood <span class="card__sep">|</span> <span class="card__role">Principal</span></div>
    <div class="card__contact"><b>P</b> : 0400 512 384 <b>|</b> <b>E</b> : maren@corvana.net.au <b>|</b> <b>ACN</b> : 012 345 678</div>
    <div class="card__bar"></div>
  </section>

  <section class="card card--back" aria-label="Business card back">
    <div class="wordmark">corvana</div>
  </section>

  <div class="detail-label">Zoom In details</div>

  <div class="detail detail--top" aria-hidden="true">
    <div class="sheet">
      <header class="sheet__header">
        <div class="wordmark">corvana</div>
        <div class="company-line">Business Consultants Pty Ltd</div>
        <div class="contact-band">
          <span class="contact-band__block"></span>
          <ul class="contact-band__list">
            <li>P : 0400 512 384</li>
            <li>E : maren@corvana.net.au</li>
            <li>ACN : 012 345 678</li>
          </ul>
        </div>
      </header>
    </div>
  </div>

  <div class="detail detail--side" aria-hidden="true">
    <div class="sheet">
      <header class="sheet__header">
        <div class="wordmark">corvana</div>
        <div class="company-line">Business Consultants Pty Ltd</div>
        <div class="contact-band">
          <span class="contact-band__block"></span>
          <ul class="contact-band__list">
            <li>P : 0400 512 384</li>
            <li>E : maren@corvana.net.au</li>
            <li>ACN : 012 345 678</li>
          </ul>
        </div>
      </header>
    </div>
  </div>

</body>
</html>
```